HollowPine Ventures Inc. Business Card Design

My business is custom renovations and homes.I would need to have a new business logo created to go along with my company name. The business card should be of a modern style as this is the market I am focused on. I would need my contact information and website posted on the card. I would also like to list a few of the tasks I conduct on the card (such as: Renovations, Additions, Repairs, New Homes, Design, Consultations). On the reverse of the card I currently have just my logo and my motto, "Shaping A Bold Path". However, I am open to completely changing everything as I am starting a new year and would like to excel further. Any new ideas and suggestions are always welcomed. Thank you.

Target Market(s)

Upscale residential and commercial renovations and builds

Industry/Entity Type

Business

Contact Information for Business Card

I would like the design to be able to be laser cut or burnt onto a wooden business card. I will be creating one option of cards for really loyal customers (wooden) and a second option for the everyday customer (paper).

Font styles to use
Other font styles liked:
• Calibri / anything of mordern taste

Colors
f37122
5c5c5c
474747
ffffff

Requirements
Must have
• I would like the colours of my business to be a sharp orange and grey. I believe this will symbolize a modern style. I am open to other suggestions if this is not suitable for the designers tastes. My contact info as follows:
• Will Marsh
• President
• HollowPine Ventures Inc.
• 555-214-3987
• will@hollowpineventures.example
• I would like my website (currently under construction) hollowpineventures.example on the card aswell.
Nice to have
• Along with a modern logo representing HollowPine, I would like something on the card besides the logo and contact information. Perhaps a small background design. I feel it may be nice to have my services listed on the card (in smaller font on the bottom) Renovations, Additions, Repairs, Design, Consultations.
Should not have
• The business card should not have too many different colors. Should not have rounded corners.

```html
<!DOCTYPE html>
<html lang="en">
<head>
<meta charset="utf-8">
<title>HollowPine Ventures Inc. Business Card</title>
<link href="https://fonts.googleapis.com/css2?family=Lato:wght@400;700&display=swap" rel="stylesheet">
<style>
  :root {
    --orange: #f37122;
    --grey: #5c5c5c;
    --grey-dark: #474747;
    --white: #ffffff;
    --ink: #1f1f1f;
    --backdrop: #2a2a2a;
  }
  html, body {
    margin: 0;
    width: 1200px;
    height: 798px;
    overflow: hidden;
    background: var(--backdrop);
    font-family: "Lato", sans-serif;
  }
  .card {
    position: absolute;
    left: 180px;
    top: 159px;
    width: 840px;
    height: 480px;
    background: var(--white);
    overflow: hidden;
  }
  .brand {
    position: absolute;
    left: 56px;
    top: 60px;
    display: flex;
    align-items: center;
    gap: 20px;
  }
  .brand-square {
    width: 62px;
    height: 62px;
    background: var(--orange);
  }
  .brand-name {
    font-size: 40px;
    font-weight: 400;
    color: var(--orange);
    letter-spacing: 1px;
    text-transform: uppercase;
  }
  .contact {
    position: absolute;
    left: 56px;
    top: 196px;
    color: var(--ink);
  }
  .contact-name {
    font-size: 27px;
    margin: 0;
  }
  .contact-title {
    font-size: 22px;
    color: var(--orange);
    margin: 0;
  }
  .contact-lines {
    margin: 28px 0 0;
    font-size: 22px;
    line-height: 1.3;
  }
  .accent-strip {
    position: absolute;
    right: 0;
    bottom: 0;
    width: 330px;
    height: 34px;
    background: var(--orange);
  }
  .services {
    position: absolute;
    left: 0;
    bottom: 0;
    width: 520px;
    height: 124px;
    background: var(--grey);
    border-top-right-radius: 22px;
    box-sizing: border-box;
    padding: 22px 0 0 30px;
    color: var(--white);
    font-size: 23px;
    line-height: 1.4;
  }
  .services p { margin: 0; }
</style>
</head>
<body>
  <div class="card">
    <div class="brand">
      <div class="brand-square"></div>
      <div class="brand-name">HollowPine Ventures</div>
    </div>

    <div class="contact">
      <p class="contact-name">Will Marsh</p>
      <p class="contact-title">President</p>
      <p class="contact-lines">555-214-3987<br>will@hollowpineventures.example</p>
    </div>

    <div class="accent-strip"></div>
    <div class="services">
      <p>• Renovations • Additions • Repairs</p>
      <p>• New Homes • Design • Consultations</p>
    </div>
  </div>
</body>
</html>
```